Flyer for International Internship Program in Dublin, Ireland

We need a one-page flyer promoting our newest internship program in Dublin, Ireland called "Venture Lantern". Northbound Placements provides international internship programs (like a study abroad) for university students. The Venture Lantern program is 10 weeks and includes full-time internship in an Irish start-up company, panel discussions with entrepreneurs and industry leaders, and a business competition along with social events and housing in Dublin. The flyer must convey the purpose of the program to university students as well as be fun and professional.
Updates

I've posted a new logo in .png format. Please let me know if there are any issues with that file. 

We've made some changes to text:

1. Please change the title to: 
Venture Lantern 
Dublin Entrepreneur Internship Program 

2. Please add the price: $7,190
3. Please add an Irish and American flag 
4. Please be sure that the color scheme is similar to that palette of the logo

Target Market(s)

We are trying to attract university students (21-23) as well as college staff like study abroad offices and advisors.

Industry/Entity Type

University

Requirements
Must have
• We would like to see flyers convey all of the content attached as well as images of Dublin, and business/professional themed photos. The flyer must have our logo (attached) and website. We'd like the information divided into sections so it looks clean and easy to read.
Nice to have
• We'd like to see some color (like our logo), but it doesn't need to be too bright or overwhelming. Young, but professional.
Should not have
• Do not use any overly styled fonts like scripts or "Celtic-looking" text.

```html
<!DOCTYPE html>
<html lang="en">
<head>
<meta charset="utf-8">
<title>Venture Lantern – Dublin Entrepreneur Internship Program</title>
<link href="https://fonts.googleapis.com/css2?family=Tinos:wght@400;700&family=Roboto+Condensed:wght@700&display=swap" rel="stylesheet">
<style>
  :root{
    --page:#ffffff;
    --ink:#1c1c1c;
    --teal:#2f6079;
    --navy:#1f3f66;
    --green:#8ba53a;
    --ribbon:#4f8db8;
    --ribbon-dark:#2f6690;
    --panel:#80bedb;
    --divider:#b5c94a;
  }
  *{box-sizing:border-box;margin:0;padding:0}
  html,body{width:1040px;height:1200px;overflow:hidden;background:var(--page)}
  body{font-family:"Tinos",serif;color:var(--ink);position:relative}
  .flyer{position:absolute;inset:0;background:var(--page)}

  .brand{position:absolute;left:70px;top:52px;display:flex;align-items:center;gap:18px}
  .brand-dot{width:96px;height:96px;border-radius:50%;background:var(--teal)}
  .brand-name{font-family:"Tinos",serif;font-size:33px;line-height:1.02;color:var(--teal);letter-spacing:.5px;text-transform:uppercase}

  .header-rule{position:absolute;left:458px;top:26px;width:5px;height:150px;background:var(--divider)}
  .flags{position:absolute;left:482px;top:30px;display:flex;gap:20px}
  .program{position:absolute;left:482px;top:76px}
  .program-title{font-size:37px;font-weight:400;color:var(--teal);text-transform:uppercase;line-height:1}
  .program-sub{font-size:25px;font-weight:700;color:var(--green);line-height:1.25;margin-top:4px}
  .program-dates{font-size:23px;color:var(--navy);line-height:1.15}

  .photos{position:absolute;left:0;top:195px;width:1040px;height:275px;display:flex;gap:3px}
  .photo{height:100%}
  .photo-abbey{width:376px;background:linear-gradient(180deg,#8f9aa6 0%,#6f7472 55%,#3f6a2e 82%,#b83a2a 100%)}
  .photo-office{width:376px;background:linear-gradient(160deg,#c8d3dc 0%,#7d8893 45%,#2e3440 100%)}
  .photo-bridge{flex:1;background:linear-gradient(180deg,#324a86 0%,#5a6aa0 45%,#c79a5a 70%,#23283a 100%)}

  .ribbon{position:absolute;top:505px;height:52px}
  .ribbon svg{position:absolute;inset:0}
  .ribbon-label{position:relative;display:block;text-align:center;line-height:44px;font-family:"Roboto Condensed",sans-serif;font-weight:700;font-size:33px;color:#fff}
  .ribbon-why{left:128px;width:320px}
  .ribbon-exp{left:585px;width:330px}

  .column{position:absolute;top:575px;font-size:17.5px;line-height:1.3}
  .column-why{left:110px;width:355px}
  .column-exp{left:492px;width:400px}
  .column-rule{position:absolute;left:480px;top:575px;width:1px;height:170px;background:#9a9a9a}

  .inclusions{position:absolute;left:108px;top:790px;width:830px;height:266px;background:var(--panel);overflow:hidden}
  .inclusions-ribbon{position:absolute;left:-58px;top:46px;width:250px;height:46px;background:var(--ribbon-dark);transform:rotate(-40deg);color:#fff;font-family:"Roboto Condensed",sans-serif;font-weight:700;font-size:28px;text-align:center;line-height:46px}
  .inclusions-list{position:absolute;left:150px;top:14px;width:460px;list-style:none;font-size:16.5px;line-height:1.15}
  .inclusions-list li{position:relative;padding-left:18px;margin-bottom:3px}
  .inclusions-list li::before{content:"";position:absolute;left:2px;top:6px;width:6px;height:6px;background:#fff;transform:rotate(45deg)}
  .inclusions-rule{position:absolute;left:625px;top:24px;width:2px;height:218px;background:#fff}
  .inclusions-icons{position:absolute;left:665px;top:24px}

  .footer-rule{position:absolute;top:1062px;width:5px;height:125px;background:var(--divider)}
  .footer-rule-fee{left:448px}
  .footer-rule-contact{left:608px}
  .apply{position:absolute;left:110px;top:1070px}
  .apply-title{font-size:47px;font-weight:700;color:var(--green);line-height:1}
  .apply-site{font-size:22px;font-weight:700;margin-top:8px}
  .fee{position:absolute;left:468px;top:1070px}
  .fee-label{font-size:17px;font-weight:700}
  .fee-amount{font-size:48px;font-weight:700;color:var(--green);line-height:1.1}
  .contact{position:absolute;left:628px;top:1070px}
  .contact-email{font-size:22px;font-weight:700}
  .contact-phone{font-size:43px;font-weight:700;line-height:1.15;margin-top:6px}
</style>
</head>
<body>
<main class="flyer">
  <header>
    <div class="brand">
      <div class="brand-dot"></div>
      <div class="brand-name">Northbound<br>Placements</div>
    </div>
    <div class="header-rule"></div>
    <div class="flags">
      <svg width="64" height="40" viewBox="0 0 64 40" role="img" aria-label="United States flag">
        <rect width="64" height="40" fill="#fff"/>
        <g fill="#b22234">
          <rect y="0" width="64" height="3.1"/><rect y="6.2" width="64" height="3.1"/><rect y="12.3" width="64" height="3.1"/>
          <rect y="18.5" width="64" height="3.1"/><rect y="24.6" width="64" height="3.1"/><rect y="30.8" width="64" height="3.1"/>
          <rect y="36.9" width="64" height="3.1"/>
        </g>
        <rect width="28" height="21.6" fill="#3c3b6e"/>
      </svg>
      <svg width="64" height="40" viewBox="0 0 64 40" role="img" aria-label="Irish flag">
        <rect width="21.4" height="40" fill="#169b62"/>
        <rect x="21.3" width="21.4" height="40" fill="#fff"/>
        <rect x="42.6" width="21.4" height="40" fill="#ff883e"/>
      </svg>
    </div>
    <div class="program">
      <h1 class="program-title">Venture Lantern</h1>
      <p class="program-sub">Dublin Entrepreneur Internship Program</p>
      <p class="program-dates">May 31 - August 9, 2014</p>
    </div>
  </header>

  <section class="photos">
    <div class="photo photo-abbey" role="img" aria-label="Photo of a grey stone Dublin college arch with red tulips in front"></div>
    <div class="photo photo-office" role="img" aria-label="Photo of young professionals meeting around a laptop in an office"></div>
    <div class="photo photo-bridge" role="img" aria-label="Photo of a lit footbridge over the River Liffey at dusk"></div>
  </section>

  <div class="ribbon ribbon-why">
    <svg width="320" height="52" viewBox="0 0 320 52">
      <polygon points="0,8 34,8 34,52 0,52 12,30" fill="var(--ribbon-dark)"/>
      <polygon points="320,8 286,8 286,52 320,52 308,30" fill="var(--ribbon-dark)"/>
      <rect x="22" y="0" width="276" height="44" fill="var(--ribbon)"/>
    </svg>
    <span class="ribbon-label">Why Dublin?</span>
  </div>
  <div class="ribbon ribbon-exp">
    <svg width="330" height="52" viewBox="0 0 330 52">
      <polygon points="0,8 34,8 34,52 0,52 12,30" fill="var(--ribbon-dark)"/>
      <polygon points="330,8 296,8 296,52 330,52 318,30" fill="var(--ribbon-dark)"/>
      <rect x="22" y="0" width="286" height="44" fill="var(--ribbon)"/>
    </svg>
    <span class="ribbon-label">The Experience</span>
  </div>

  <p class="column column-why">Dublin is at the heart of new European investment in business innovation and we can't imagine a better place to launch your career. As the European headquarters for many of the leading tech and social media corporations, the city is gaining traction as a dynamic place to create and grow business.</p>
  <div class="column-rule"></div>
  <p class="column column-exp">Northbound Placements wants to help young professionals embrace Dublin's entrepreneurship. Along with a full-time internship in Irish start-ups, interns will tour companies like Corvane Systems, have discussions with industry leaders and partake in a business competition complete with prizes.</p>

  <section class="inclusions">
    <div class="inclusions-ribbon">Inclusions</div>
    <ul class="inclusions-list">
      <li>Centralized housing in Harbourview College Dublin.</li>
      <li>Guaranteed internship withing a startup or entrepreneurial enterprise.</li>
      <li>Panel Discussions.</li>
      <li>Site visits with companies including Corvane Systems.</li>
      <li>Networking events.</li>
      <li>Entrepreneurship challenge with prizes.</li>
      <li>Social events and excursions.</li>
      <li>24/7 on the ground staff support.</li>
      <li>Career development and access to the Keystone Strengths Profile assessment.</li>
    </ul>
    <div class="inclusions-rule"></div>
    <svg class="inclusions-icons" width="140" height="220" viewBox="0 0 140 220" fill="none" stroke="#fff" stroke-width="3">
      <circle cx="60" cy="30" r="22" fill="#fff"/>
      <path d="M46 22 q8 -6 14 2 q-4 8 4 12 q-8 8 -14 0z M64 14 q10 2 14 10 q-8 2 -10 -4z" fill="var(--panel)" stroke="none"/>
      <path d="M86 40 q30 30 -8 62" stroke-dasharray="5 5"/>
      <rect x="40" y="95" width="46" height="32" rx="2"/>
      <path d="M56 127 v8 M70 127 v8 M50 137 h26"/>
      <path d="M40 120 q-30 25 4 55" stroke-dasharray="5 5"/>
      <g transform="rotate(40 60 185)">
        <rect x="52" y="160" width="16" height="40" fill="#fff" stroke="none"/>
        <polygon points="52,200 68,200 60,214" fill="#fff" stroke="none"/>
      </g>
    </svg>
  </section>

  <footer>
    <div class="apply">
      <p class="apply-title">APPLY NOW</p>
      <p class="apply-site">www.northboundplacements.com</p>
    </div>
    <div class="footer-rule footer-rule-fee"></div>
    <div class="fee">
      <p class="fee-label">Registration Fee</p>
      <p class="fee-amount">$7,190</p>
    </div>
    <div class="footer-rule footer-rule-contact"></div>
    <div class="contact">
      <p class="contact-email">info@northboundplacements.com</p>
      <p class="contact-phone">1-410-555-0148</p>
    </div>
  </footer>
</main>
</body>
</html>
```